CFO services graphic design

I own a business consulting firm called Marlowe Consulting and we need a graphic for CFO services in our colours and branding. The attached file "CFO services to be put into Marlowe consulting theme", shows the content for the design. The two other files show the theme and colours for the new design.

```html
<!DOCTYPE html>
<html lang="en">
<head>
<meta charset="utf-8">
<title>CFO Services – Marlowe Consulting</title>
<link href="https://fonts.googleapis.com/css2?family=Poppins:wght@300;400;500;700;800&display=swap" rel="stylesheet">
<style>
  :root {
    --frame: #023f5a;
    --panel: #ececec;
    --ink: #222426;
    --brand-orange: #f7931e;
    --core-orange: #f54b00;
    --white: #ffffff;
    --number: #1b1b1b;
  }
  html, body {
    margin: 0;
    padding: 0;
    width: 1200px;
    height: 1200px;
    overflow: hidden;
    background: var(--frame);
  }
  .canvas {
    display: block;
    width: 1200px;
    height: 1200px;
    font-family: "Poppins", sans-serif;
  }
  .headline { font-weight: 500; font-size: 50px; fill: var(--ink); letter-spacing: 1px; }
  .headline .accent { font-weight: 700; fill: var(--brand-orange); }
  .brand-name { font-weight: 300; font-size: 46px; fill: var(--brand-orange); letter-spacing: 1px; }
  .blade-title { font-weight: 700; font-size: 33px; fill: var(--white); }
  .blade-note { font-weight: 400; font-size: 26px; fill: var(--white); }
  .step-number { font-weight: 700; font-size: 38px; fill: var(--number); text-anchor: middle; }
  .core-label { font-weight: 700; font-size: 35px; fill: var(--white); text-anchor: middle; }
  .icon { fill: var(--white); }
  .icon-stroke { fill: none; stroke: var(--white); stroke-width: 6; stroke-linecap: round; stroke-linejoin: round; }
</style>
</head>
<body>
<svg class="canvas" viewBox="0 0 1932 1932" xmlns="http://www.w3.org/2000/svg">
  <defs>
    <linearGradient id="grad-orange" x1="0" y1="0" x2="0" y2="1">
      <stop offset="0" stop-color="#ffab0a"/>
      <stop offset="1" stop-color="#f64806"/>
    </linearGradient>
    <linearGradient id="grad-orange-up" x1="0" y1="1" x2="0" y2="0">
      <stop offset="0" stop-color="#ffab0a"/>
      <stop offset="1" stop-color="#f65a06"/>
    </linearGradient>
    <linearGradient id="grad-blue" x1="0" y1="0" x2="0" y2="1">
      <stop offset="0" stop-color="#6a93ea"/>
      <stop offset="1" stop-color="#2248c0"/>
    </linearGradient>
    <linearGradient id="grad-blue-up" x1="0" y1="1" x2="0" y2="0">
      <stop offset="0" stop-color="#5a86e2"/>
      <stop offset="1" stop-color="#1c47bd"/>
    </linearGradient>
    <linearGradient id="grad-teal" x1="0" y1="0" x2="0" y2="1">
      <stop offset="0" stop-color="#006a9a"/>
      <stop offset="1" stop-color="#00adeb"/>
    </linearGradient>
    <linearGradient id="grad-navy" x1="0" y1="0" x2="0" y2="1">
      <stop offset="0" stop-color="#0a3f93"/>
      <stop offset="1" stop-color="#012357"/>
    </linearGradient>
    <linearGradient id="grad-navy-down" x1="0" y1="0" x2="0" y2="1">
      <stop offset="0" stop-color="#01214f"/>
      <stop offset="1" stop-color="#0448a0"/>
    </linearGradient>
    <linearGradient id="grad-panel" x1="0" y1="0" x2="1" y2="1">
      <stop offset="0" stop-color="#f1f1f1"/>
      <stop offset="0.5" stop-color="#e9e9e9"/>
      <stop offset="1" stop-color="#f0f0f0"/>
    </linearGradient>
  </defs>

  <!-- frame and panel -->
  <rect class="frame" width="1932" height="1932" fill="var(--frame)"/>
  <rect class="panel" x="120" y="120" width="1693" height="1693" fill="url(#grad-panel)"/>

  <!-- headline -->
  <text class="headline" x="215" y="250">CFO SERVICES TO BE PUT</text>
  <text class="headline" x="215" y="310">INTO <tspan class="accent">MARLOWE CONSULTING</tspan></text>

  <!-- brand -->
  <g class="brand">
    <circle cx="1380" cy="265" r="50" fill="var(--brand-orange)"/>
    <text class="brand-name" x="1450" y="266">MARLOWE</text>
    <text class="brand-name" x="1450" y="314">CONSULTING</text>
  </g>

  <!-- blades -->
  <g class="blades">
    <polygon class="blade blade-cost" points="1065,520 1545,522 1065,1002" fill="url(#grad-orange)"/>
    <polygon class="blade blade-capital" points="1385,740 1722,1083 1042,1083" fill="url(#grad-navy)"/>
    <polygon class="blade blade-investment" points="1460,1110 1460,1590 980,1110" fill="url(#grad-teal)"/>
    <polygon class="blade blade-performance" points="897,1090 1240,1433 897,1770" fill="url(#grad-blue-up)"/>
    <polygon class="blade blade-budgeting" points="867,1030 867,1510 387,1510" fill="url(#grad-orange-up)"/>
    <polygon class="blade blade-risk" points="215,945 890,945 548,1287" fill="url(#grad-navy-down)"/>
    <polygon class="blade blade-compliance" points="475,437 475,915 953,915" fill="url(#grad-teal)"/>
    <polygon class="blade blade-communication" points="1037,262 1037,940 697,600" fill="url(#grad-blue)"/>
  </g>

  <!-- hub -->
  <circle class="hub-ring" cx="969" cy="1013" r="241" fill="var(--white)"/>
  <g class="hub-dividers" stroke="#2d6fd0" stroke-width="2" opacity="0.6">
    <line x1="1037" y1="790" x2="1037" y2="890"/>
    <line x1="1180" y1="930" x2="1110" y2="1000"/>
    <line x1="1200" y1="1083" x2="1095" y2="1083"/>
    <line x1="1055" y1="1200" x2="1005" y2="1150"/>
    <line x1="897" y1="1240" x2="897" y2="1140"/>
    <line x1="760" y1="1100" x2="830" y2="1030"/>
    <line x1="740" y1="945" x2="840" y2="945"/>
    <line x1="860" y1="800" x2="935" y2="875"/>
  </g>
  <g class="step-numbers">
    <text class="step-number" x="1105" y="902">1</text>
    <text class="step-number" x="1160" y="1033">2</text>
    <text class="step-number" x="1093" y="1172">3</text>
    <text class="step-number" x="953" y="1218">4</text>
    <text class="step-number" x="825" y="1165">5</text>
    <text class="step-number" x="772" y="1018">6</text>
    <text class="step-number" x="840" y="884">7</text>
    <text class="step-number" x="985" y="840">8</text>
  </g>
  <circle class="hub-core" cx="969" cy="1013" r="143" fill="var(--core-orange)"/>
  <text class="core-label" x="969" y="980">CHIEF</text>
  <text class="core-label" x="969" y="1023">FINANCIAL</text>
  <text class="core-label" x="969" y="1066">OFFICER</text>

  <!-- blade text -->
  <g class="blade-copy">
    <text class="blade-title" x="753" y="570">Communication</text>
    <text class="blade-note" x="770" y="605">Board of Directors,</text>
    <text class="blade-note" x="770" y="635">creditors, owners,</text>
    <text class="blade-note" x="780" y="665">investors, credit</text>
    <text class="blade-note" x="810" y="695">rating agencies</text>

    <text class="blade-title" x="1107" y="595">Cost</text>
    <text class="blade-title" x="1107" y="633">Accounting</text>
    <text class="blade-title" x="1107" y="671">&amp; Cost</text>
    <text class="blade-title" x="1107" y="709">Management</text>

    <text class="blade-title" x="1300" y="915">Captial</text>
    <text class="blade-title" x="1300" y="953">Structure</text>
    <text class="blade-title" x="1300" y="991">and the Cost</text>
    <text class="blade-title" x="1300" y="1029">of Capital</text>

    <text class="blade-title" x="1200" y="1189">Long-term &amp;</text>
    <text class="blade-title" x="1200" y="1227">short-term</text>
    <text class="blade-title" x="1200" y="1265">investment</text>
    <text class="blade-title" x="1200" y="1303">decisions</text>

    <text class="blade-title" x="941" y="1414">Performance</text>
    <text class="blade-title" x="941" y="1452">Evaluation</text>

    <text class="blade-title" x="629" y="1336">Budgeting</text>
    <text class="blade-title" x="629" y="1374">&amp; Strategic</text>
    <text class="blade-title" x="629" y="1412">Planning</text>

    <text class="blade-title" x="447" y="1064">Risk</text>
    <text class="blade-title" x="447" y="1102">Management</text>

    <text class="blade-title" x="507" y="720">Compliance</text>
    <text class="blade-note" x="507" y="756">Tax, legal and</text>
    <text class="blade-note" x="507" y="786">regulatory</text>
  </g>

  <!-- icons -->
  <g class="icons">
    <g class="icon-chat">
      <ellipse class="icon" cx="930" cy="442" rx="24" ry="22"/>
      <ellipse class="icon" cx="952" cy="460" rx="22" ry="20"/>
      <circle cx="920" cy="442" r="3" fill="#4a74d8"/><circle cx="930" cy="442" r="3" fill="#4a74d8"/><circle cx="940" cy="442" r="3" fill="#4a74d8"/>
    </g>
    <g class="icon-document">
      <rect class="icon" x="510" y="575" width="42" height="58" rx="4"/>
      <path class="icon" d="M555 598 l15 14 v8 c0 10-8 16-15 20 c-7-4-15-10-15-20 v-8z"/>
      <path d="M549 618 l4 4 l8-8" stroke="#0a7fbd" stroke-width="3" fill="none"/>
    </g>
    <g class="icon-ledger">
      <rect class="icon" x="1388" y="553" width="36" height="50" rx="4"/>
      <circle class="icon" cx="1430" cy="593" r="16"/>
      <text x="1430" y="601" font-size="20" font-weight="700" text-anchor="middle" fill="#fb9b0c" font-family="Poppins, sans-serif">$</text>
    </g>
    <g class="icon-capital">
      <circle class="icon" cx="1585" cy="1000" r="10"/>
      <circle class="icon-stroke" cx="1598" cy="1018" r="9" stroke-width="4"/>
      <path class="icon-stroke" d="M1555 1040 l20 10 h22 l12-14"/>
    </g>
    <g class="icon-investment">
      <path class="icon-stroke" d="M1380 1440 h20 M1397 1425 l-10 -10 l-10 10 M1405 1432 q10-15 20-5"/>
      <ellipse class="icon" cx="1397" cy="1455" rx="26" ry="8"/>
      <ellipse class="icon" cx="1397" cy="1468" rx="26" ry="8"/>
    </g>
    <g class="icon-gauge">
      <path class="icon" d="M933 1642 a35 35 0 0 1 70 0 z"/>
      <path d="M968 1642 l22 -18" stroke="#4877dc" stroke-width="5"/>
      <path class="icon" d="M968 1575 l3 7 l7 1 l-5 5 l1 7 l-6 -3 l-6 3 l1 -7 l-5 -5 l7 -1z"/>
      <path class="icon" d="M944 1585 l2 5 l5 1 l-4 3 l1 5 l-4 -2 l-4 2 l1 -5 l-4 -3 l5 -1z"/>
      <path class="icon" d="M992 1585 l2 5 l5 1 l-4 3 l1 5 l-4 -2 l-4 2 l1 -5 l-4 -3 l5 -1z"/>
    </g>
    <g class="icon-strategy">
      <circle class="icon-stroke" cx="512" cy="1448" r="22"/>
      <rect class="icon" x="500" y="1438" width="24" height="34"/>
      <rect class="icon" x="497" y="1475" width="30" height="10"/>
    </g>
    <g class="icon-risk">
      <path class="icon-stroke" d="M325 1025 a27 27 0 1 1 50 0"/>
      <path class="icon" d="M350 990 l24 44 h-48z"/>
      <rect x="347" y="1005" width="6" height="16" fill="#01285e"/>
      <circle cx="350" cy="1027" r="3.5" fill="#01285e"/>
    </g>
  </g>
</svg>
</body>
</html>
```